We have a new logo so we need to change our business card

We're super Happy with our current cards but I think with a new logo should come a new design. I wouldn't mind seeing the icons that we used on the back last time reused on this card. Please feel free to visit our website to get a sense for our brand www.pawlowtide.ca

I need the final final to have contact info for:

Derek Osgood
Co-Owner
info@pawlowtide.ca
604-315-2780

and

Melissa Osgood
Co-Owner
info@pawlowtide.ca
604-347-5138

Target Market(s)

Female dog owners, 21 to 70

Industry/Entity Type

pet industry

Contact Information for Business Card

included in brief

Requirements
Should not have
• We do not want it to look cartonish

```html
<!DOCTYPE html>
<html lang="en">
<head>
<meta charset="utf-8">
<title>Pawlowtide Business Card</title>
<link href="https://fonts.googleapis.com/css2?family=Open+Sans:wght@700;800&family=Arimo:wght@400&display=swap" rel="stylesheet">
<style>
  :root {
    --page-bg: #dcdcdc;
    --card-black: #0b0c0c;
    --card-white: #ffffff;
    --brand-green: #8cc63f;
    --pale-green: #dcedc8;
    --pattern-tone: #1c2321;
    --logo-grey: #3d3a39;
    --text-white: #ffffff;
  }
  * { margin: 0; padding: 0; box-sizing: border-box; }
  html, body { width: 1200px; height: 900px; overflow: hidden; }
  body {
    background: var(--page-bg);
    font-family: "Arimo", Arial, sans-serif;
    position: relative;
  }
  .card {
    position: absolute;
    left: 280px;
    width: 640px;
    height: 366px;
    overflow: hidden;
    box-shadow: 0 6px 18px rgba(0,0,0,0.25);
  }
  .card-back { top: 62px; background: var(--card-black); }
  .card-front { top: 470px; background: var(--card-white); }

  .back-pattern {
    position: absolute; inset: 0;
    background: radial-gradient(circle at 50% 50%, var(--pattern-tone) 0%, #121615 70%, var(--card-black) 100%);
  }
  .back-mark {
    position: absolute; left: 292px; top: 52px;
    width: 58px; height: 58px; border-radius: 50%;
    background: var(--brand-green);
  }

  .front-art { position: absolute; inset: 0; }

  .brand {
    position: absolute; right: 38px; top: 40px;
    display: flex; align-items: center; gap: 10px;
  }
  .brand-dot { width: 48px; height: 48px; border-radius: 50%; background: var(--brand-green); flex: none; }
  .brand-name {
    font-family: "Open Sans", sans-serif; font-weight: 700;
    font-size: 34px; line-height: 1; color: var(--logo-grey); letter-spacing: -0.5px;
  }

  .contact-list {
    position: absolute; right: 26px; top: 138px;
    list-style: none; text-align: right;
  }
  .contact-list li {
    display: flex; justify-content: flex-end; align-items: center; gap: 10px;
    color: var(--text-white); font-size: 15px; line-height: 21px;
  }
  .contact-list svg { width: 14px; height: 14px; flex: none; }
  .contact-list .social { width: 13px; height: 13px; background: var(--brand-green); border-radius: 3px; flex: none; margin: 0 0.5px; }

  .person { position: absolute; left: 86px; bottom: 42px; }
  .person-name {
    font-family: "Open Sans", sans-serif; font-weight: 800;
    font-size: 27px; color: var(--brand-green); line-height: 1.05;
  }
  .person-role { font-size: 15px; color: var(--text-white); }
</style>
</head>
<body>

<section class="card card-back">
  <div class="back-pattern" role="img" aria-label="Repeating tone-on-tone pattern of the brand mark on black"></div>
  <div class="back-mark"></div>
</section>

<section class="card card-front">
  <svg class="front-art" viewBox="0 0 640 366" width="640" height="366">
    <circle cx="170" cy="150" r="150" fill="var(--pale-green)" role="img" aria-label="Large faint brand mark of a dog silhouette"/>
    <path d="M0,262 C170,310 300,262 390,178 C470,108 560,96 640,94 L640,366 L0,366 Z" fill="var(--card-black)"/>
    <path d="M0,256 C170,304 300,256 390,172 C470,102 560,90 640,88" fill="none" stroke="var(--brand-green)" stroke-width="5"/>
  </svg>

  <div class="brand">
    <div class="brand-dot"></div>
    <span class="brand-name">Pawlowtide</span>
  </div>

  <ul class="contact-list">
    <li>604-315-2780
      <svg viewBox="0 0 24 24"><path d="M6.6 10.8a15 15 0 0 0 6.6 6.6l2.2-2.2a1 1 0 0 1 1-.25 11.4 11.4 0 0 0 3.6.57 1 1 0 0 1 1 1V20a1 1 0 0 1-1 1A17 17 0 0 1 3 4a1 1 0 0 1 1-1h3.5a1 1 0 0 1 1 1c0 1.25.2 2.45.57 3.6a1 1 0 0 1-.25 1z" fill="var(--brand-green)"/></svg>
    </li>
    <li>info@pawlowtide.ca
      <svg viewBox="0 0 24 24"><rect x="2" y="5" width="20" height="14" rx="1" fill="var(--brand-green)"/><path d="M2 6l10 7 10-7" fill="none" stroke="var(--card-black)" stroke-width="1.6"/></svg>
    </li>
    <li>www.pawlowtide.ca
      <svg viewBox="0 0 24 24" fill="none" stroke="var(--brand-green)" stroke-width="1.8"><circle cx="12" cy="12" r="10"/><ellipse cx="12" cy="12" rx="4.5" ry="10"/><path d="M2 12h20M4 7h16M4 17h16"/></svg>
    </li>
    <li>@Pawlowtide <span class="social"></span></li>
    <li>Pawlowtide <span class="social"></span></li>
  </ul>

  <div class="person">
    <div class="person-name">Derek Osgood</div>
    <div class="person-role">Co-Owner</div>
  </div>
</section>

</body>
</html>
```